Brindlewick Music Studio needs a promotional postcard design

We are looking for a postcard design for a small business that provides clients with private music lesson instruction. We are looking for a design that will convey the message of "music is fun for kids" that will appeal to parents and encourage them to sign up. We have a company logo that should be used and our color scheme is teal and turquoise. All of our contact info should be displayed as well.

Target Market(s)

Parents with young kids

Contact Information for Business Card

web: www.brindlewickmusicstudio.example
email: lessons@brindlewickmusicstudio.example
phone: 202-555-0147

Font styles to use
Serif
Sans Serif

Colors
33b8a4
86cfc6
0456a4
87cfc6

Requirements
Must have
• Music lessons in your home
• Creating little stars one at a time
• Sign Up Now
• Please use these images:
Nice to have
• Something like this sample postcard:

```html
<!DOCTYPE html>
<html lang="en">
<head>
<meta charset="utf-8">
<title>Brindlewick Music Studio – Postcard</title>
<link href="https://fonts.googleapis.com/css2?family=Montserrat:wght@400;800&family=Open+Sans:wght@600;700&family=Libre+Baskerville&display=swap" rel="stylesheet">
<style>
  :root {
    --teal: #33b8a4;
    --aqua: #86cfc6;
    --blue: #0456a4;
    --deep-blue: #1a4f94;
    --white: #ffffff;
    --backdrop: #eeeae5;
    --photo-warm: #b67f45;
  }
  * { box-sizing: border-box; margin: 0; padding: 0; }
  html, body { width: 1200px; height: 785px; overflow: hidden; }
  body { background: var(--backdrop); position: relative; font-family: "Open Sans", sans-serif; }

  .postcard {
    position: absolute;
    width: 447px;
    height: 344px;
    overflow: hidden;
    box-shadow: 0 4px 14px rgba(0,0,0,0.22);
  }

  /* ---------- Front ---------- */
  .postcard--front {
    left: 410px; top: 41px;
    background: linear-gradient(120deg, #6f6a66 0%, #2f6a9c 45%, var(--blue) 100%);
  }
  .front__instrument-photo {
    position: absolute; left: 0; top: 0; width: 447px; height: 190px;
    background: linear-gradient(100deg, var(--photo-warm) 0%, #c9a075 22%, #7d8c9a 50%, rgba(60,110,160,0.3) 75%, rgba(4,86,164,0) 100%);
  }
  .front__piano-photo {
    position: absolute; left: 230px; top: 190px; width: 217px; height: 100px;
    background: linear-gradient(90deg, rgba(210,225,240,0) 0%, rgba(205,222,240,0.45) 55%, rgba(160,190,225,0.35) 100%);
  }
  .front__group-photo {
    position: absolute; left: 0; top: 108px; width: 268px; height: 236px;
    border-top-right-radius: 150px 130px;
    background: linear-gradient(160deg, #3b3a48 0%, #5d4d57 45%, #2a2730 100%);
  }
  .photo-circle {
    position: absolute; border-radius: 50%;
    border: 2px solid var(--white);
    box-shadow: 0 0 0 4px rgba(255,255,255,0.25);
  }
  .photo-circle--violinist {
    left: 100px; top: 37px; width: 116px; height: 116px;
    background: radial-gradient(circle at 50% 55%, #4a3b3a 0%, #141216 70%);
  }
  .photo-circle--singer {
    left: 209px; top: 192px; width: 84px; height: 84px;
    background: radial-gradient(circle at 50% 45%, #c8b6a8 0%, #5a4c4a 75%);
  }
  .orbit-line {
    position: absolute; left: 0; top: 0; width: 447px; height: 344px; pointer-events: none;
  }

  .brand { position: absolute; display: flex; align-items: center; white-space: nowrap; }
  .brand__badge { border-radius: 50%; flex: none; }
  .brand__name {
    font-family: "Libre Baskerville", serif;
    font-weight: 400;
    line-height: 1;
  }
  .brand__name small {
    display: block; font-size: 8px; letter-spacing: 4px; margin-top: 6px;
  }
  .postcard--front .brand { left: 222px; top: 17px; }
  .postcard--front .brand__badge {
    width: 58px; height: 58px; background: var(--white);
    border: 3px solid var(--teal); margin-right: 12px;
  }
  .postcard--front .brand__name { color: var(--white); font-size: 21px; }

  .headline {
    position: absolute; right: 12px; top: 122px;
    font-family: "Montserrat", sans-serif; color: var(--white);
    font-size: 27px; line-height: 34px; text-align: right; font-weight: 400;
    white-space: nowrap;
  }
  .headline strong { font-weight: 800; }

  .contact-strip {
    position: absolute; color: var(--white);
    display: flex; flex-direction: column; justify-content: center;
    white-space: nowrap;
  }
  .contact-strip__row { display: flex; align-items: center; gap: 5px; font-size: 6.5px; font-weight: 600; line-height: 14px; }
  .contact-strip__row--phone { font-size: 19px; font-weight: 700; line-height: 22px; }
  .contact-strip__icon { width: 9px; height: 9px; flex: none; }
  .contact-strip__row--phone .contact-strip__icon { width: 12px; height: 12px; }

  .postcard--front .contact-strip {
    left: 254px; top: 282px; width: 193px; height: 62px;
    padding-left: 18px;
    clip-path: polygon(12px 0, 100% 0, 100% 100%, 0 100%);
    background: linear-gradient(90deg, var(--teal) 0%, #1d7fb0 45%, var(--blue) 100%);
  }

  /* ---------- Back ---------- */
  .postcard--back { left: 674px; top: 408px; background: var(--white); }
  .back__recital-photo {
    position: absolute; left: 0; top: 0; width: 260px; height: 344px;
    background: linear-gradient(180deg, #8a5a2e 0%, #5d3a1f 30%, #1c1a22 60%, #141319 100%);
  }
  .postcard--back .contact-strip {
    left: 0; top: 292px; width: 270px; height: 52px;
    padding-left: 34px;
    background: linear-gradient(90deg, var(--deep-blue) 0%, #1d6ea8 55%, var(--teal) 100%);
  }
  .postcard--back .contact-strip__row--phone { font-size: 18px; line-height: 21px; }
  .back__curve { position: absolute; left: 0; top: 0; width: 447px; height: 344px; }
  .postcard--back .brand { left: 242px; top: 15px; }
  .postcard--back .brand__badge {
    width: 26px; height: 26px; border: 2px solid var(--teal); margin-right: 6px;
  }
  .postcard--back .brand__name { color: var(--teal); font-size: 12px; }
  .postcard--back .brand__name small { font-size: 4px; letter-spacing: 2.4px; margin-top: 3px; }
  .stamp-box {
    position: absolute; left: 375px; top: 14px; width: 58px; height: 54px;
    border: 1px solid #555;
  }
  .address-line {
    position: absolute; left: 280px; width: 148px; height: 0;
    border-top: 1px solid #666;
  }
  .address-line--1 { top: 213px; }
  .address-line--2 { top: 241px; }
  .address-line--3 { top: 269px; }
</style>
</head>
<body>

<section class="postcard postcard--front">
  <div class="front__instrument-photo" role="img" aria-label="Close-up photo of flute keys in warm golden light"></div>
  <div class="front__piano-photo" role="img" aria-label="Faded photo of piano keys and sheet music"></div>
  <div class="front__group-photo" role="img" aria-label="Photo of a group of smiling children with their music teacher after a recital"></div>

  <svg class="orbit-line" viewBox="0 0 447 344" aria-hidden="true">
    <path d="M40 102 Q120 70 215 92 Q280 115 292 232" fill="none" stroke="#2f7fd0" stroke-width="1"/>
    <circle cx="158" cy="95" r="68" fill="none" stroke="rgba(255,255,255,0.7)" stroke-width="0.8"/>
  </svg>

  <div class="photo-circle photo-circle--violinist" role="img" aria-label="Photo of a young girl playing violin on stage"></div>
  <div class="photo-circle photo-circle--singer" role="img" aria-label="Photo of a cheerful girl singing"></div>

  <div class="brand">
    <span class="brand__badge"></span>
    <span class="brand__name">Brindlewick<small>MUSIC STUDIO</small></span>
  </div>

  <h1 class="headline"><strong>MUSIC</strong> IS FUN<br>FOR <strong>KIDS</strong></h1>

  <div class="contact-strip">
    <div class="contact-strip__row">
      <svg class="contact-strip__icon" viewBox="0 0 10 10"><circle cx="5" cy="5" r="4.4" fill="none" stroke="#fff" stroke-width="0.9"/><ellipse cx="5" cy="5" rx="1.8" ry="4.4" fill="none" stroke="#fff" stroke-width="0.7"/><line x1="0.6" y1="5" x2="9.4" y2="5" stroke="#fff" stroke-width="0.7"/></svg>
      <span>www.brindlewickmusicstudio.example</span>
    </div>
    <div class="contact-strip__row">
      <svg class="contact-strip__icon" viewBox="0 0 10 10"><circle cx="5" cy="5" r="4.4" fill="none" stroke="#fff" stroke-width="0.9"/><rect x="2.6" y="3.3" width="4.8" height="3.4" fill="none" stroke="#fff" stroke-width="0.7"/><path d="M2.6 3.3 L5 5.3 L7.4 3.3" fill="none" stroke="#fff" stroke-width="0.7"/></svg>
      <span>lessons@brindlewickmusicstudio.example</span>
    </div>
    <div class="contact-strip__row contact-strip__row--phone">
      <svg class="contact-strip__icon" viewBox="0 0 12 12"><path d="M2.5 1 L4.5 1 L5.3 3.6 L4 4.6 Q5 7 7.4 8 L8.4 6.7 L11 7.5 L11 9.5 Q10.5 11 9 11 Q1 10 1 2.5 Q1 1 2.5 1 Z" fill="#fff"/></svg>
      <span>202-555-0147</span>
    </div>
  </div>
</section>

<section class="postcard postcard--back">
  <div class="back__recital-photo" role="img" aria-label="Photo of a girl in a white dress playing a grand piano at a recital, with a teacher and student behind"></div>

  <div class="contact-strip">
    <div class="contact-strip__row">
      <svg class="contact-strip__icon" viewBox="0 0 10 10"><circle cx="5" cy="5" r="4.4" fill="none" stroke="#fff" stroke-width="0.9"/><ellipse cx="5" cy="5" rx="1.8" ry="4.4" fill="none" stroke="#fff" stroke-width="0.7"/><line x1="0.6" y1="5" x2="9.4" y2="5" stroke="#fff" stroke-width="0.7"/></svg>
      <span>www.brindlewickmusicstudio.example</span>
    </div>
    <div class="contact-strip__row">
      <svg class="contact-strip__icon" viewBox="0 0 10 10"><circle cx="5" cy="5" r="4.4" fill="none" stroke="#fff" stroke-width="0.9"/><rect x="2.6" y="3.3" width="4.8" height="3.4" fill="none" stroke="#fff" stroke-width="0.7"/><path d="M2.6 3.3 L5 5.3 L7.4 3.3" fill="none" stroke="#fff" stroke-width="0.7"/></svg>
      <span>lessons@brindlewickmusicstudio.example</span>
    </div>
    <div class="contact-strip__row contact-strip__row--phone">
      <svg class="contact-strip__icon" viewBox="0 0 12 12"><path d="M2.5 1 L4.5 1 L5.3 3.6 L4 4.6 Q5 7 7.4 8 L8.4 6.7 L11 7.5 L11 9.5 Q10.5 11 9 11 Q1 10 1 2.5 Q1 1 2.5 1 Z" fill="#fff"/></svg>
      <span>202-555-0147</span>
    </div>
  </div>

  <svg class="back__curve" viewBox="0 0 447 344" aria-hidden="true">
    <path d="M218 0 Q318 172 210 344 L447 344 L447 0 Z" fill="#ffffff"/>
    <path d="M224 0 Q324 172 216 344" fill="none" stroke="#0456a4" stroke-width="1"/>
  </svg>

  <div class="brand">
    <span class="brand__badge"></span>
    <span class="brand__name">Brindlewick<small>MUSIC STUDIO</small></span>
  </div>

  <div class="stamp-box"></div>
  <div class="address-line address-line--1"></div>
  <div class="address-line address-line--2"></div>
  <div class="address-line address-line--3"></div>
</section>

</body>
</html>
```